stationary for hygienic company

We need a stationary design for hygienic company which provides public high end sanitary products and high end public lavatory.
We need a fresh and clean style stationary
we want the following things:
* logo (redesigned in eps/vector)
* Letterhead (with company details)
* letterhead (without company details)
* Business card
* note block
* ballpoint
* etcetera (a complete package)

```html
<!DOCTYPE html>
<html lang="en">
<head>
<meta charset="utf-8">
<title>Lumiva Envelope Stationery</title>
<link href="https://fonts.googleapis.com/css2?family=Open+Sans:wght@400;600&display=swap" rel="stylesheet">
<style>
  :root {
    --backdrop: #f1f1f1;
    --paper: #ffffff;
    --fold: #e3e3e3;
    --edge: #dcdcdc;
    --ink: #222222;
    --ink-soft: #555555;
    --accent-pink: #e2467f;
    --accent-blue: #5ab8dc;
    --window: #f6f6f6;
  }
  * { margin: 0; padding: 0; box-sizing: border-box; }
  html, body { width: 1200px; height: 1000px; overflow: hidden; }
  body {
    background: var(--backdrop);
    font-family: "Open Sans", Arial, sans-serif;
    color: var(--ink);
    position: relative;
  }
  .envelope {
    position: absolute;
    width: 600px;
    height: 300px;
    background: var(--paper);
    border: 1px solid var(--edge);
    box-shadow: 0 10px 30px rgba(0,0,0,0.08);
  }
  .envelope--back { left: 90px; top: 120px; }
  .envelope--front { left: 510px; top: 560px; }

  .flap-line {
    position: absolute;
    left: 0; right: 0; top: 62px;
    border-top: 1px solid var(--fold);
  }
  .brand {
    display: flex;
    align-items: center;
    gap: 6px;
  }
  .brand__dot {
    width: 14px; height: 14px;
    border-radius: 50%;
    background: var(--accent-pink);
    flex: none;
  }
  .brand__name {
    font-weight: 600;
    color: var(--ink);
  }
  .brand-block--back {
    position: absolute;
    right: 30px; bottom: 60px;
    text-align: right;
  }
  .brand-block--back .brand__name { font-size: 15px; }
  .brand-block--back .tagline { font-size: 7px; color: var(--ink-soft); margin-top: 2px; }

  .window {
    position: absolute;
    right: 40px; top: 80px;
    width: 220px; height: 110px;
    background: var(--window);
    border: 1px solid var(--edge);
  }
  .sender {
    position: absolute;
    left: 30px; bottom: 30px;
  }
  .sender .brand__name { font-size: 20px; }
  .sender .brand__dot { width: 20px; height: 20px; }
  .tagline--front { font-size: 9px; font-weight: 600; margin: 6px 0 4px; }
  .contact { list-style: none; font-size: 8px; color: var(--ink-soft); line-height: 1.6; }
  .contact li { display: flex; align-items: center; gap: 6px; }
  .contact svg { width: 8px; height: 8px; flex: none; fill: var(--accent-blue); }
</style>
</head>
<body>
  <section class="envelope envelope--back" aria-label="Envelope back">
    <div class="flap-line"></div>
    <div class="brand-block--back">
      <div class="brand"><span class="brand__dot"></span><span class="brand__name">Lumiva</span></div>
      <div class="tagline">Boutique Hygiénique</div>
    </div>
  </section>

  <section class="envelope envelope--front" aria-label="Envelope front">
    <div class="window"></div>
    <div class="sender">
      <div class="brand"><span class="brand__dot"></span><span class="brand__name">Lumiva</span></div>
      <div class="tagline--front">Boutique Hygiénique</div>
      <ul class="contact">
        <li><svg viewBox="0 0 10 10"><path d="M5 0a3.5 3.5 0 0 0-3.5 3.5C1.5 6 5 10 5 10s3.5-4 3.5-6.5A3.5 3.5 0 0 0 5 0zm0 5a1.5 1.5 0 1 1 0-3 1.5 1.5 0 0 1 0 3z"/></svg>123 Main Street, Anytown,<br>Postal Code, Country</li>
        <li><svg viewBox="0 0 10 10"><path d="M2 0l2 2-1 1.5a6 6 0 0 0 3.5 3.5L8 6l2 2-1.5 2C4 10 0 6 0 1.5z"/></svg>555-1234-56</li>
        <li><svg viewBox="0 0 10 10"><rect x="0" y="2" width="10" height="6"/></svg>email@youraddress.com</li>
        <li><svg viewBox="0 0 10 10"><circle cx="5" cy="5" r="5"/></svg>www.yourwebsite.com</li>
      </ul>
    </div>
  </section>
</body>
</html>
```